Corvane Electrical Solutions

On one side. LOGO (underneath:) Commercial Industrial Residential

- NAME & CONTACT DETAILS

Marcus T. Hollings
Project Manager

(Cell icon) (441) 582-6197
(Email icon) cvnelectricalsoultions@mailventra.com
(Facebook & Instagram icons )@cvnelectricalsolutions

Other side: LOGO - underneath ELECTRICAL CONSTRUCTION & MAINTENANCE . LED LIGHTING & AUTOMATION . LIFE SAFETY SYSTEMS (FIRE ALARM / SECURITY) . DATA & COMMUNICATION

```html
<!DOCTYPE html>
<html lang="en">
<head>
<meta charset="utf-8">
<title>Corvane Electrical Solutions – Business Card</title>
<link rel="stylesheet" href="https://fonts.googleapis.com/css2?family=Montserrat:wght@500;600;700&family=Arimo:wght@400&display=swap">
<style>
  :root {
    --teal: #165a70;
    --graphite: #4a4a4a;
    --ink: #3a3a3a;
    --paper: #ffffff;
    --backdrop: #2f3438;
  }
  * { box-sizing: border-box; margin: 0; padding: 0; }
  html, body {
    width: 1200px; height: 1000px; overflow: hidden;
    background: var(--backdrop);
  }
  .card {
    position: absolute;
    left: 220px;
    width: 760px; height: 434px;
    background: var(--paper);
    border-radius: 22px;
    overflow: hidden;
  }
  .card--services { top: 36px; }
  .card--contact  { top: 522px; }

  /* brand block */
  .brand {
    position: absolute;
    display: flex; align-items: center; gap: 18px;
  }
  .brand__mark {
    width: 22px; height: 22px; background: var(--teal);
  }
  .brand__name {
    font-family: "Montserrat", sans-serif;
    font-weight: 600;
    color: var(--teal);
    font-size: 34px;
    line-height: 1.12;
    letter-spacing: 5px;
    text-transform: uppercase;
  }
  .card--services .brand { top: 70px; left: 200px; }
  .card--contact  .brand { top: 56px; left: 200px; }

  /* services side */
  .services-band {
    position: absolute; left: 0; right: 0; bottom: 0; height: 150px;
    background: var(--teal);
    border-top: 8px solid var(--graphite);
  }
  .services {
    list-style: none;
    position: absolute; left: 52px; right: 40px; top: 34px;
    display: grid; grid-template-columns: 1.25fr 1fr;
    row-gap: 22px; column-gap: 24px;
    font-family: "Montserrat", sans-serif; font-weight: 500;
    font-size: 14px; letter-spacing: 0.4px;
    color: var(--paper); text-transform: uppercase;
  }
  .services li { display: flex; align-items: center; gap: 10px; white-space: nowrap; }
  .services li::before {
    content: ""; width: 8px; height: 8px; border: 1.5px solid var(--paper);
    border-radius: 50%; flex: none;
  }

  /* contact side */
  .person {
    position: absolute; left: 56px; top: 262px; width: 300px; text-align: right;
  }
  .person__name {
    font-family: "Montserrat", sans-serif; font-weight: 700;
    color: var(--teal); font-size: 30px; letter-spacing: 0.5px;
  }
  .person__role {
    font-family: "Arimo", sans-serif; color: var(--ink); font-size: 18px; margin-top: 4px;
  }
  .divider {
    position: absolute; left: 378px; top: 252px; width: 2px; height: 118px;
    background: var(--teal);
  }
  .contacts {
    list-style: none; position: absolute; left: 396px; top: 252px;
    font-family: "Arimo", sans-serif; font-size: 17px; color: var(--ink);
    display: flex; flex-direction: column; gap: 9px;
  }
  .contacts li { display: flex; align-items: center; gap: 10px; white-space: nowrap; }
  .contacts svg { width: 14px; height: 14px; flex: none; }
  .contacts .social-dot { width: 12px; height: 12px; background: var(--ink); border-radius: 2px; flex: none; margin: 0 1px; }

  .edge-teal {
    position: absolute; left: 0; bottom: 0; width: 390px; height: 14px;
    background: var(--teal);
    clip-path: polygon(0 0, 100% 0, 97% 100%, 0 100%);
  }
  .edge-graphite {
    position: absolute; right: 0; bottom: 0; width: 380px; height: 14px;
    background: var(--graphite);
    clip-path: polygon(3% 0, 100% 0, 100% 100%, 0 100%);
  }
</style>
</head>
<body>

<section class="card card--services" aria-label="Card side with services">
  <div class="brand">
    <span class="brand__mark"></span>
    <p class="brand__name">Corvane<br>Electrical<br>Solutions</p>
  </div>
  <div class="services-band">
    <ul class="services">
      <li>Electrical Construction &amp; Maintenance</li>
      <li>LED Lighting &amp; Automation</li>
      <li>Life Safety Systems (Fire Alarm / Security)</li>
      <li>Data &amp; Communication</li>
    </ul>
  </div>
</section>

<section class="card card--contact" aria-label="Card side with contact details">
  <div class="brand">
    <span class="brand__mark"></span>
    <p class="brand__name">Corvane<br>Electrical<br>Solutions</p>
  </div>

  <div class="person">
    <p class="person__name">Marcus T. Hollings</p>
    <p class="person__role">Project Manager</p>
  </div>
  <div class="divider"></div>

  <ul class="contacts">
    <li>
      <svg viewBox="0 0 24 24" aria-hidden="true"><path fill="#165a70" d="M6.6 10.8a15.1 15.1 0 0 0 6.6 6.6l2.2-2.2a1 1 0 0 1 1-.25 11.4 11.4 0 0 0 3.6.57 1 1 0 0 1 1 1V20a1 1 0 0 1-1 1A17 17 0 0 1 3 4a1 1 0 0 1 1-1h3.5a1 1 0 0 1 1 1c0 1.25.2 2.45.57 3.57a1 1 0 0 1-.25 1z"/></svg>
      (441) 582-6197
    </li>
    <li>
      <svg viewBox="0 0 24 24" aria-hidden="true"><path fill="#165a70" d="M2 5h20v14H2z"/><path fill="none" stroke="#fff" stroke-width="1.8" d="M2.5 5.5 12 13l9.5-7.5"/></svg>
      cvnelectricalsoultions@mailventra.com
    </li>
    <li><span class="social-dot"></span>@cvnelectricalsolutions</li>
    <li><span class="social-dot"></span>@cvnelectricalsolutions</li>
  </ul>

  <div class="edge-teal"></div>
  <div class="edge-graphite"></div>
</section>

</body>
</html>
```